User Interface Design for new Team Management App

We're developing a new app with a unique, two part, user interface. The artistic section of our UI is complete, we now need the functional part completed. The functional part will include menus, inputting data, scrolling and etc. We have our own developers and coders, so no need to worry about that.

The contest:
The artist we decide to work with will submit a design which will be their vision for the entirety of the project. See the brief for more information, it is attached.

Points to remember:
-We like artists to submit fast
-Please follow the brief
-Please show examples of other UI work you have completed in the past
-We like people who communicate promptly, openly and professionally.

Thank you, and good luck.

Industry/Entity Type

Management

```html
<!DOCTYPE html>
<html lang="en">
<head>
<meta charset="utf-8">
<title>CrewCards – Profile Setup</title>
<link rel="stylesheet" href="https://fonts.googleapis.com/css2?family=Montserrat:wght@400;600;700&family=Open+Sans:wght@300;400&family=Cinzel:wght@700&display=swap">
<style>
  :root {
    --backdrop: #e4e6e8;
    --status-brown: #b98455;
    --panel-cream: #cfca98;
    --panel-border: #a8703f;
    --field-ochre: #b9a65a;
    --label-ink: #2f2a1c;
    --placeholder: #f4efd6;
    --arrow-brown: #8a4a22;
    --accent-blue: #2f6fb3;
    --save-red: #c4532a;
    --strip-olive: #6d681f;
    --screen-dark: #2b2618;
  }
  * { box-sizing: border-box; margin: 0; padding: 0; }
  html, body { width: 1200px; height: 1200px; overflow: hidden; }
  body { background: var(--backdrop); position: relative; font-family: "Open Sans", sans-serif; }

  .app-screen {
    position: absolute; left: 300px; top: 66px; width: 600px; height: 1067px;
    background: var(--panel-cream); border: 3px solid var(--screen-dark); overflow: hidden;
  }

  .status-bar {
    position: absolute; left: 0; top: 0; width: 100%; height: 40px; background: var(--status-brown);
    color: #fff; font-family: "Open Sans", sans-serif; font-size: 16px; display: flex; align-items: center;
    padding: 0 14px; justify-content: space-between;
  }
  .status-bar .carrier { display: flex; align-items: center; gap: 6px; }
  .status-bar .clock { position: absolute; left: 50%; transform: translateX(-50%); }
  .status-bar .battery { display: flex; align-items: center; gap: 8px; }

  .profile-panel {
    position: absolute; left: 8px; top: 48px; width: 578px; height: 730px;
    border: 2px solid var(--panel-border); background: var(--panel-cream);
  }

  .close-button { position: absolute; right: 22px; top: 22px; }

  .header-rule { position: absolute; top: 40px; height: 2px; width: 150px; background: var(--screen-dark); }
  .header-rule.left { left: 120px; }
  .header-rule.right { right: 120px; }
  .avatar {
    position: absolute; left: 50%; top: 16px; width: 60px; height: 60px; margin-left: -30px;
    border-radius: 50%; background: radial-gradient(circle at 50% 40%, #5a4e46, #26201c);
    border: 2px solid var(--panel-cream);
  }

  .form-row { position: absolute; left: 0; width: 100%; height: 46px; }
  .form-label {
    position: absolute; right: 392px; top: 0; height: 46px; display: flex; align-items: center;
    font-family: "Montserrat", sans-serif; font-weight: 700; font-size: 17px; color: var(--label-ink);
    text-align: right; line-height: 1.05;
  }
  .field {
    position: absolute; top: 0; height: 46px; background: var(--field-ochre);
    display: flex; align-items: center; justify-content: space-between; padding: 0 12px;
    color: var(--placeholder); font-size: 16px; font-weight: 300;
  }
  .field.wide { left: 200px; width: 356px; }
  .field.day { left: 200px; width: 96px; }
  .field.month { left: 306px; width: 120px; }
  .field.year { left: 436px; width: 120px; }
  .field .value { font-weight: 400; }
  .dropdown-icon { flex: none; }

  .photo-drop {
    position: absolute; left: 200px; top: 0; width: 62px; height: 62px; background: var(--field-ochre);
    display: flex; align-items: center; justify-content: center;
  }

  .source-question {
    position: absolute; left: 200px; top: 568px; font-family: "Montserrat", sans-serif;
    font-weight: 600; font-size: 16px; color: var(--label-ink);
  }
  .source-select { top: 596px; }

  .save-button { position: absolute; left: 134px; top: 656px; }

  .card-strip {
    position: absolute; left: 8px; top: 790px; width: 578px; height: 266px; background: var(--strip-olive);
    display: flex; gap: 6px; padding: 8px;
  }
  .story-card { flex: 1; background: #f5f2e6; padding: 5px; display: flex; flex-direction: column; }
  .card-art { flex: 1; }
  .card-art.you { background: linear-gradient(180deg, #8fb3cf 0%, #6d7a74 55%, #4b3f30 100%); }
  .card-art.team { background: linear-gradient(180deg, #a9c3d8 0%, #6a5a58 55%, #3d3a3a 100%); }
  .card-art.mission { background: linear-gradient(180deg, #c9d6df 0%, #8a9070 50%, #9a7a3a 100%); }
  .card-art.strategy { background: linear-gradient(180deg, #b9cde0 0%, #4f6b3a 50%, #7a5a3a 100%); }
  .card-title {
    height: 30px; display: flex; align-items: center; justify-content: center;
    font-family: "Cinzel", serif; font-weight: 700; font-size: 12px; color: #1d1a14; letter-spacing: 0.5px;
  }
</style>
</head>
<body>
  <main class="app-screen">
    <header class="status-bar">
      <span class="carrier">●●●○○ Nmobile
        <svg width="18" height="14" viewBox="0 0 18 14"><path d="M1 5a12 12 0 0 1 16 0M4 8a7.5 7.5 0 0 1 10 0M7 11a3 3 0 0 1 4 0" fill="none" stroke="#fff" stroke-width="1.8" stroke-linecap="round"/></svg>
      </span>
      <span class="clock">11:27 AM</span>
      <span class="battery">
        <svg width="10" height="16" viewBox="0 0 10 16"><path d="M1 4l8 8-4 3V1l4 3-8 8" fill="none" stroke="#fff" stroke-width="1.4"/></svg>
        <svg width="30" height="14" viewBox="0 0 30 14"><rect x="0.5" y="0.5" width="26" height="13" rx="2" fill="#fff"/><rect x="27.5" y="4" width="2" height="6" fill="#fff"/></svg>
      </span>
    </header>

    <section class="profile-panel">
      <svg class="close-button" width="34" height="34" viewBox="0 0 34 34" aria-label="Close">
        <circle cx="17" cy="17" r="15" fill="none" stroke="var(--accent-blue)" stroke-width="2"/>
        <path d="M11 11l12 12M23 11L11 23" stroke="var(--accent-blue)" stroke-width="3" stroke-linecap="round"/>
      </svg>

      <span class="header-rule left"></span>
      <span class="header-rule right"></span>
      <div class="avatar" role="img" aria-label="Hooded character avatar"></div>

      <div class="form-row" style="top:106px">
        <label class="form-label">Name</label>
        <div class="field wide">Type here...</div>
      </div>
      <div class="form-row" style="top:164px">
        <label class="form-label">Occupation</label>
        <div class="field wide">Select here
          <svg class="dropdown-icon" width="24" height="24" viewBox="0 0 24 24"><circle cx="12" cy="12" r="10" fill="none" stroke="var(--arrow-brown)" stroke-width="2"/><path d="M7 9h10l-5 7z" fill="var(--arrow-brown)"/></svg>
        </div>
      </div>
      <div class="form-row" style="top:222px">
        <label class="form-label">Birthday</label>
        <div class="field day"><span class="value">03</span>
          <svg class="dropdown-icon" width="24" height="24" viewBox="0 0 24 24"><circle cx="12" cy="12" r="10" fill="none" stroke="var(--arrow-brown)" stroke-width="2"/><path d="M7 9h10l-5 7z" fill="var(--arrow-brown)"/></svg>
        </div>
        <div class="field month">Month
          <svg class="dropdown-icon" width="24" height="24" viewBox="0 0 24 24"><circle cx="12" cy="12" r="10" fill="none" stroke="var(--arrow-brown)" stroke-width="2"/><path d="M7 9h10l-5 7z" fill="var(--arrow-brown)"/></svg>
        </div>
        <div class="field year">Year
          <svg class="dropdown-icon" width="24" height="24" viewBox="0 0 24 24"><circle cx="12" cy="12" r="10" fill="none" stroke="var(--arrow-brown)" stroke-width="2"/><path d="M7 9h10l-5 7z" fill="var(--arrow-brown)"/></svg>
        </div>
      </div>
      <div class="form-row" style="top:280px">
        <label class="form-label">Nationality</label>
        <div class="field wide">Select here
          <svg class="dropdown-icon" width="24" height="24" viewBox="0 0 24 24"><circle cx="12" cy="12" r="10" fill="none" stroke="var(--arrow-brown)" stroke-width="2"/><path d="M7 9h10l-5 7z" fill="var(--arrow-brown)"/></svg>
        </div>
      </div>
      <div class="form-row" style="top:338px">
        <label class="form-label">E*mail</label>
        <div class="field wide">Type here...</div>
      </div>
      <div class="form-row" style="top:396px">
        <label class="form-label">Mobile</label>
        <div class="field wide"><span class="value">01020004471</span></div>
      </div>
      <div class="form-row" style="top:460px">
        <label class="form-label">Headshot<br>Photo</label>
        <div class="photo-drop">
          <svg width="28" height="28" viewBox="0 0 28 28" aria-label="Add photo"><circle cx="14" cy="14" r="12" fill="none" stroke="var(--accent-blue)" stroke-width="2"/><path d="M14 8v12M8 14h12" stroke="var(--accent-blue)" stroke-width="2.4" stroke-linecap="round"/></svg>
        </div>
      </div>

      <p class="source-question">How did you find out about CrewCards?</p>
      <div class="form-row source-select">
        <div class="field wide">Select here
          <svg class="dropdown-icon" width="24" height="24" viewBox="0 0 24 24"><circle cx="12" cy="12" r="10" fill="none" stroke="var(--arrow-brown)" stroke-width="2"/><path d="M7 9h10l-5 7z" fill="var(--arrow-brown)"/></svg>
        </div>
      </div>

      <svg class="save-button" width="310" height="60" viewBox="0 0 310 60" aria-label="Save">
        <path d="M4 30L44 6v48zM306 30L266 6v48z" fill="none" stroke="var(--save-red)" stroke-width="1.6"/>
        <path d="M44 10h222l-10 20 10 20H44l10-20z" fill="none" stroke="var(--save-red)" stroke-width="1.6"/>
        <text x="155" y="38" text-anchor="middle" font-family="Montserrat, sans-serif" font-weight="700" font-size="22" fill="var(--save-red)">SAVE</text>
      </svg>
    </section>

    <section class="card-strip">
      <article class="story-card"><div class="card-art you" role="img" aria-label="Painted scene of a hooded traveller in a landscape"></div><h3 class="card-title">THE YOU CARD</h3></article>
      <article class="story-card"><div class="card-art team" role="img" aria-label="Painted scene of a group of companions"></div><h3 class="card-title">THE TEAM CARD</h3></article>
      <article class="story-card"><div class="card-art mission" role="img" aria-label="Painted mountain valley landscape"></div><h3 class="card-title">THE MISSION CARD</h3></article>
      <article class="story-card"><div class="card-art strategy" role="img" aria-label="Painted scene of a council gathered under a tree"></div><h3 class="card-title">THE STRATEGY CARD</h3></article>
    </section>
  </main>
</body>
</html>
```